CareJure Chambers Mailer for Small Medical Offices and Solo Physician Practices

CareJure Chambers -- We are a local health law firm looking to provide advice to medical practices on the legal issues they face. We strive to function as a general counsel for medical practices and provide tailored solutions to meet the needs of our clients. Please see postcard content ideas in document attached. Our firm colors are royal blue, gray and white and black.

Target Market(s)

Small medical offices, solo physician practices in the Southeast Michigan (Detroit Metro area)

Industry/Entity Type

Law Firm

Font styles to use
Sans Serif

Colors
0991cd
3176b5
ffffff
7f7f7f
1b1b1b

Requirements
Must have
• Brief summary of legal services offered, bullet pointed list of practice areas/issues
• Contact information, website, address
• Pictures of attorneys
• Prefer the use of our firm's colors (royal blue, gray, white, black)
Nice to have
• Included some purchased stock images that could also be incorporated

```html
<!DOCTYPE html>
<html lang="en">
<head>
<meta charset="utf-8">
<title>CareJure Chambers Mailer</title>
<link rel="stylesheet" href="https://fonts.googleapis.com/css2?family=Jost:wght@400;500;700;800&family=Lato:wght@300;400;700&display=swap">
<style>
  :root {
    --stage: #4a4848;
    --royal: #0a67b3;
    --sky: #1aa3e2;
    --sky-dark: #0f2d5a;
    --tick: #3cb4ee;
    --divider: #3f3f41;
    --white: #ffffff;
    --gray: #7f7f7f;
    --ink: #1b1b1b;
    --photo-deep: #1d3d80;
    --photo-mid: #7a8ea8;
    --photo-light: #e9e6df;
  }
  * { margin: 0; padding: 0; box-sizing: border-box; }
  html, body { width: 1200px; height: 727px; overflow: hidden; }
  body { background: var(--stage); font-family: "Lato", sans-serif; position: relative; }

  .postcard {
    position: absolute; left: 92px; top: 86px;
    width: 1016px; height: 554px;
    background: var(--white); overflow: hidden;
  }
  .postcard-photo {
    position: absolute; inset: 0;
    clip-path: polygon(400px 0, 1016px 0, 1016px 440px, 540px 440px);
    background: linear-gradient(135deg, var(--photo-deep) 0%, var(--photo-mid) 45%, var(--photo-light) 80%, #b58a55 100%);
  }
  .postcard-divider {
    position: absolute; inset: 0;
    clip-path: polygon(392px 0, 410px 0, 600px 554px, 578px 554px);
    background: var(--divider);
  }
  .postcard-panel {
    position: absolute; inset: 0;
    clip-path: polygon(0 0, 392px 0, 578px 554px, 0 554px);
    background: var(--royal);
    color: var(--white);
  }

  .headline {
    position: absolute; left: 36px; top: 30px;
    font-family: "Jost", sans-serif; font-weight: 800;
    font-size: 53px; line-height: 46px; letter-spacing: 0.5px;
    color: var(--sky);
    text-shadow: 3px 3px 0 var(--sky-dark);
  }
  .intro, .service-note {
    position: absolute; left: 38px; width: 380px;
    font-size: 13.6px; line-height: 15.6px; font-weight: 400;
  }
  .intro { top: 144px; }
  .service-note { top: 368px; }

  .service-list {
    position: absolute; left: 38px; top: 199px;
    list-style: none;
    font-weight: 700; font-size: 13.6px; line-height: 15.5px;
  }
  .service-list li { padding-left: 19px; position: relative; }
  .service-list svg { position: absolute; left: 0; top: 3px; width: 12px; height: 10px; }

  .consult-banner {
    position: absolute; left: 36px; top: 429px;
    width: 268px; height: 24px;
    background: var(--sky);
    clip-path: polygon(0 0, 256px 0, 268px 24px, 0 24px);
    font-weight: 700; font-size: 13.5px; letter-spacing: 0.3px;
    line-height: 24px; padding-left: 7px;
  }

  .firm-name { position: absolute; left: 40px; top: 467px; font-weight: 700; font-size: 13.6px; }
  .contact-row { position: absolute; display: flex; align-items: flex-start; font-size: 13.6px; line-height: 16px; }
  .contact-row svg { width: 13px; height: 13px; margin-right: 8px; margin-top: 1px; flex: none; }
  .contact-address { left: 38px; top: 491px; }
  .contact-phone { left: 305px; top: 473px; font-weight: 700; font-size: 14px; }
  .contact-email { left: 305px; top: 491px; }
  .contact-web { left: 326px; top: 509px; font-weight: 700; color: #9fdcff; }

  .firm-mark {
    position: absolute; left: 626px; top: 455px;
    display: flex; align-items: center; gap: 14px;
    font-family: "Lato", sans-serif; font-weight: 700;
    font-size: 38px; color: var(--gray); letter-spacing: 0.2px;
  }
  .firm-mark-square { width: 22px; height: 22px; background: var(--royal); }
</style>
</head>
<body>
  <div class="postcard">
    <div class="postcard-photo" role="img" aria-label="Stock photo of a stethoscope and wooden gavel resting on a blue leather-bound book"></div>
    <div class="postcard-divider"></div>

    <section class="postcard-panel">
      <h1 class="headline">HEALTH LAW<br>QUESTIONS?</h1>
      <p class="intro">We are local, experienced health lawyers available to provide efficient, effective advice on the issues impacting your healthcare business every day, including:</p>

      <ul class="service-list">
        <li><svg viewBox="0 0 12 10"><path d="M1 5l3.5 3.5L11 1.5" fill="none" stroke="var(--tick)" stroke-width="2.4"/></svg>Contract review and negotiation</li>
        <li><svg viewBox="0 0 12 10"><path d="M1 5l3.5 3.5L11 1.5" fill="none" stroke="var(--tick)" stroke-width="2.4"/></svg>Stark and Anti-kickback matters</li>
        <li><svg viewBox="0 0 12 10"><path d="M1 5l3.5 3.5L11 1.5" fill="none" stroke="var(--tick)" stroke-width="2.4"/></svg>Reimbursement and payer issues</li>
        <li><svg viewBox="0 0 12 10"><path d="M1 5l3.5 3.5L11 1.5" fill="none" stroke="var(--tick)" stroke-width="2.4"/></svg>HIPAA</li>
        <li><svg viewBox="0 0 12 10"><path d="M1 5l3.5 3.5L11 1.5" fill="none" stroke="var(--tick)" stroke-width="2.4"/></svg>Vendor issues</li>
        <li><svg viewBox="0 0 12 10"><path d="M1 5l3.5 3.5L11 1.5" fill="none" stroke="var(--tick)" stroke-width="2.4"/></svg>Licensing matters</li>
        <li><svg viewBox="0 0 12 10"><path d="M1 5l3.5 3.5L11 1.5" fill="none" stroke="var(--tick)" stroke-width="2.4"/></svg>Employee issues</li>
        <li><svg viewBox="0 0 12 10"><path d="M1 5l3.5 3.5L11 1.5" fill="none" stroke="var(--tick)" stroke-width="2.4"/></svg>Difficult patient matters</li>
        <li><svg viewBox="0 0 12 10"><path d="M1 5l3.5 3.5L11 1.5" fill="none" stroke="var(--tick)" stroke-width="2.4"/></svg>Subpoenas and medical record requests</li>
        <li><svg viewBox="0 0 12 10"><path d="M1 5l3.5 3.5L11 1.5" fill="none" stroke="var(--tick)" stroke-width="2.4"/></svg>Leases and landlord-tenant issues</li>
      </ul>

      <p class="service-note">We provide personalized service to our clients so you have trusted counsel available when you need it.&nbsp; We offer competitive hourly rates as well as flat fee arrangements when possible.</p>

      <div class="consult-banner">FREE CONSULTATIONS AVAILABLE:</div>

      <div class="firm-name">CareJure Chambers</div>
      <div class="contact-row contact-address">
        <svg viewBox="0 0 14 14"><circle cx="7" cy="7" r="7" fill="var(--tick)"/><path d="M7 3a2.6 2.6 0 0 0-2.6 2.6C4.4 7.6 7 11 7 11s2.6-3.4 2.6-5.4A2.6 2.6 0 0 0 7 3z" fill="var(--royal)"/><circle cx="7" cy="5.6" r="1" fill="var(--tick)"/></svg>
        <span>18420 Meridian Road, Suite 310<br>Southfield, MI 48076</span>
      </div>
      <div class="contact-row contact-phone">
        <svg viewBox="0 0 14 14"><circle cx="7" cy="7" r="7" fill="var(--tick)"/><path d="M4.3 3.6l1.5-.4.9 2-1 .8a6 6 0 0 0 2.3 2.3l.8-1 2 .9-.4 1.5c-3.4.2-6.3-2.7-6.1-6.1z" fill="var(--royal)"/></svg>
        <span>248.555.0137</span>
      </div>
      <div class="contact-row contact-email">
        <svg viewBox="0 0 14 14"><circle cx="7" cy="7" r="7" fill="var(--tick)"/><rect x="3.5" y="4.5" width="7" height="5" fill="var(--royal)"/><path d="M3.5 4.5L7 7.3l3.5-2.8" fill="none" stroke="var(--tick)" stroke-width="0.9"/></svg>
        <span>info@carejurechambers.com</span>
      </div>
      <div class="contact-row contact-web"><span>www.carejurechambers.com</span></div>
    </section>

    <div class="firm-mark">
      <span>CareJure Chambers</span>
      <span class="firm-mark-square"></span>
    </div>
  </div>
</body>
</html>
```